DJ / Music Prod. studio needs Website.

Web Design needed for a DJ / Music Production Studio. Bright crisp colors, sharp, and user friendly. The design should incorporate the equalizer look that the logo has, however I am not opposed to a different idea if you feel it would look better. When someone gets to the landing page I need them to understand what our services our immediately and be able to easily navigate the content, via both text and the view trail video which will be provided and should be the centerpiece of the landing page. thx good luck!

Target Market(s)

people hosting personal parties and events.

Industry/Entity Type

Party Planning

Logo Text

SpinFreeHost.net

Number of Pages Required

4 page

Font styles to use
Sans Serif

Colors
0592cd
e24096
a54499
6b449b
00a990
000000
86cfc6

Requirements
Must have
• A page where they can submit the info directly on the site. Fill in the blanks type and coinwell button upon submission. A video box linked to our viewtrail account on the main page so the viewtrail videos to play. The 4 pages plus landing page are; 1. Pricing 2. Submit (which is also the pay page) 3 FAQ 4. Contact. Our logo can be the header, and the mirrored one could possibly be the background. I am very open minded and open to creative suggestions. you know what looks best better then I would. Please stay with the same color scheme as the main logo. I will have the full text up within a day or 2. Thx 4 reading and good luck!
Nice to have
• Each pages header the same but in a different color scheme. See zip file
Should not have
• Anything that might take away from it being sharp , clean, and user friendly. This isn't a club dj site but more of a site for everyday people of all demographics who need music for their personal parties and events.

```html
<!DOCTYPE html>
<html lang="en">
<head>
<meta charset="utf-8">
<title>SpinFreeHost.net – What is SpinFreeHost.net</title>
<link rel="stylesheet" href="https://fonts.googleapis.com/css2?family=Exo+2:wght@400;600;700&family=Open+Sans:wght@400;600;700&display=swap">
<style>
  :root{
    --blue:#0592cd;
    --pink:#e24096;
    --violet:#a54499;
    --purple:#6b449b;
    --teal:#00a990;
    --mint:#86cfc6;
    --black:#000000;
    --glow:#0c3f9e;
    --bar-top:#3b3b3b;
    --bar-bottom:#0d0d0d;
    --text-soft:#d8d8d8;
    --text-grey:#8a8a8a;
    --frame:#c8c8c8;
  }
  *{margin:0;padding:0;box-sizing:border-box}
  html,body{width:843px;height:1200px;overflow:hidden;background:var(--black)}
  body{position:relative;font-family:"Open Sans",Arial,sans-serif;color:var(--text-soft)}

  .hero-backdrop{position:absolute;left:0;top:0;width:843px;height:555px;
    background:
      radial-gradient(ellipse 460px 300px at 421px 330px, rgba(20,90,210,.85) 0%, rgba(12,50,140,.55) 45%, rgba(0,0,0,0) 80%),
      radial-gradient(ellipse 300px 140px at 421px 40px, rgba(60,60,140,.35), rgba(0,0,0,0) 80%),
      var(--black);}

  .brand{position:absolute;top:110px;left:0;width:843px;text-align:center;
    font-family:"Exo 2",Arial,sans-serif;font-weight:700;font-size:30px;color:var(--purple);letter-spacing:.5px}

  .social{position:absolute;top:56px;left:628px;display:flex;gap:14px}
  .social-item{display:flex;flex-direction:column;align-items:center;gap:3px;font-size:8px;color:var(--text-grey)}
  .social-item .chip{width:24px;height:24px;border-radius:3px}
  .chip-kinbook{background:#3b5998}
  .chip-chirpr{background:#28aae1}
  .chip-viewtrail{background:#d8262d}

  .main-nav{position:absolute;top:170px;left:0;width:843px;height:24px;
    background:linear-gradient(var(--bar-top),var(--bar-bottom));box-shadow:0 3px 6px rgba(0,0,0,.7)}
  .nav-link{position:absolute;top:6px;font-size:10px;font-weight:600;color:#fff;letter-spacing:.5px}
  .nav-link.is-active{color:var(--pink)}
  .nav-tab{position:absolute;top:156px;left:246px;width:351px;height:42px}
  .nav-tab-label{position:absolute;top:161px;left:246px;width:351px;text-align:center;
    font-family:"Exo 2",Arial,sans-serif;font-weight:700;font-size:17px;color:#fff;letter-spacing:2px}

  .video-player{position:absolute;left:210px;top:198px;width:422px;height:210px;
    background:linear-gradient(#e2e2e2,#9d9d9d);padding:6px;border-radius:2px;box-shadow:0 4px 14px rgba(0,0,0,.6)}
  .video-screen{position:relative;width:100%;height:184px;background:#050505}
  .video-controls{height:14px;background:linear-gradient(#5a5a5a,#2c2c2c);display:flex;align-items:center;padding:0 6px;gap:6px}
  .video-progress{flex:1;height:3px;background:#777;position:relative}
  .video-progress span{position:absolute;left:0;top:0;height:3px;width:18%;background:#d22}
  .play-button{position:absolute;left:50%;top:50%;width:64px;height:64px;transform:translate(-50%,-50%)}

  .intro{position:absolute;top:420px;left:110px;width:623px;text-align:center;font-size:9.5px;line-height:14px;color:var(--text-soft)}

  .divider{position:absolute;left:0;width:843px;height:1px;
    background:linear-gradient(90deg,rgba(120,120,120,0),rgba(170,170,170,.8) 50%,rgba(120,120,120,0))}

  .eq-strip{position:absolute;left:350px;width:143px;height:26px;
    background:linear-gradient(90deg,rgba(107,68,155,0),var(--purple) 30%,var(--violet) 50%,var(--blue) 70%,rgba(5,146,205,0));
    opacity:.55;border-radius:2px}

  .section-title{position:absolute;left:0;width:843px;text-align:center;
    font-family:"Exo 2",Arial,sans-serif;font-weight:600;font-size:13px;letter-spacing:1px;color:var(--mint)}

  .benefits{position:absolute;top:648px;left:100px;width:660px;display:grid;grid-template-columns:300px 300px;column-gap:55px;row-gap:22px;list-style:none}
  .benefit{position:relative;padding-left:16px;font-size:9.5px;line-height:13px}
  .benefit::before{content:"";position:absolute;left:0;top:4px;width:6px;height:6px;border-radius:50%;background:var(--teal)}
  .benefit strong{display:block;color:var(--teal);font-weight:700}
  .benefit span{color:var(--text-grey)}

  .testimonial{position:absolute;top:960px;width:300px;display:flex;gap:18px;align-items:center}
  .avatar{flex:none;width:76px;height:76px;border-radius:50%;border:3px solid #ddd;
    background:radial-gradient(circle at 50% 45%,#c9a488,#5a3a2a)}
  .quote{font-size:10px;line-height:14px;color:var(--teal);font-weight:600}
  .quote cite{display:block;margin-top:4px;font-style:normal;color:var(--blue);font-size:9.5px}

  .site-footer{position:absolute;top:1140px;left:0;width:843px;height:38px;
    background:linear-gradient(var(--bar-top),var(--bar-bottom));box-shadow:0 -2px 8px rgba(0,0,0,.6);
    text-align:center;font-size:10px;line-height:38px;color:#e6e6e6;letter-spacing:.5px}
</style>
</head>
<body>
  <div class="hero-backdrop" role="img" aria-label="Deep blue spotlight glow over a dark tiled floor"></div>

  <header>
    <div class="brand">SpinFreeHost.net</div>
    <div class="social">
      <div class="social-item"><div class="chip chip-kinbook"></div>kinbook</div>
      <div class="social-item"><div class="chip chip-chirpr"></div>chirpr</div>
      <div class="social-item"><div class="chip chip-viewtrail"></div>viewtrail</div>
    </div>

    <nav class="main-nav">
      <a class="nav-link is-active" style="left:84px">PRICING</a>
      <a class="nav-link" style="left:148px">SUBMIT</a>
      <a class="nav-link" style="left:652px">FAQ</a>
      <a class="nav-link" style="left:700px">CONTACT</a>
    </nav>
    <svg class="nav-tab" viewBox="0 0 351 42" aria-hidden="true">
      <defs>
        <linearGradient id="tabFill" x1="0" y1="0" x2="0" y2="1">
          <stop offset="0" stop-color="#4a4a4a"/>
          <stop offset="1" stop-color="#111"/>
        </linearGradient>
      </defs>
      <path d="M0 0 H351 L336 42 H15 Z" fill="url(#tabFill)" stroke="#666" stroke-width="1"/>
    </svg>
    <div class="nav-tab-label">WHAT IS SpinFreeHost.net</div>
  </header>

  <main>
    <section class="video-player" aria-label="Featured viewtrail video">
      <div class="video-screen">
        <svg class="play-button" viewBox="0 0 64 64" aria-hidden="true">
          <circle cx="32" cy="32" r="29" fill="rgba(40,40,40,.85)" stroke="#fff" stroke-width="3"/>
          <path d="M25 18 L47 32 L25 46 Z" fill="#fff"/>
        </svg>
      </div>
      <div class="video-controls">
        <svg width="8" height="8" viewBox="0 0 8 8" aria-hidden="true"><path d="M1 0 L8 4 L1 8 Z" fill="#ddd"/></svg>
        <div class="video-progress"><span></span></div>
        <svg width="10" height="8" viewBox="0 0 10 8" aria-hidden="true"><rect x="0" y="0" width="10" height="8" fill="none" stroke="#ddd"/></svg>
      </div>
    </section>

    <p class="intro">Our studio brings professional sound to your private party without the cost of hiring a live DJ. Pick your songs, set the mood and we build a seamless mix ready to play. Weddings, birthdays, backyard gatherings and office events all sound better with a mix tailored to your guests and your night. Watch the video above to see how it works from start to finish.</p>

    <div class="divider" style="top:555px"></div>

    <section>
      <div class="eq-strip" style="top:570px" role="img" aria-label="Equalizer bars graphic"></div>
      <h2 class="section-title" style="top:600px">PRO OF SFH OVER HIRING A DJ</h2>
      <ul class="benefits">
        <li class="benefit"><strong>Save hundreds compared with booking a live DJ</strong><span>one flat price covers your full custom mix</span></li>
        <li class="benefit"><strong>No setup, no gear, no guest list space</strong><span>just press play and enjoy the party with friends</span></li>
        <li class="benefit"><strong>Your own playlist, mixed by a real producer</strong><span>every request blended smoothly from track to track</span></li>
        <li class="benefit"><strong>Clean edits for family friendly gatherings</strong><span>perfect for all ages and every kind of crowd</span></li>
        <li class="benefit"><strong>Ready days before your event, no stress</strong><span>download it and play it on any speaker system</span></li>
        <li class="benefit"><strong>Simple online ordering and secure payment</strong><span>fill in the form and check out in minutes</span></li>
      </ul>
    </section>

    <div class="divider" style="top:838px"></div>

    <section>
      <div class="eq-strip" style="top:852px" role="img" aria-label="Equalizer bars graphic"></div>
      <h2 class="section-title" style="top:882px">WHAT OUR CLIENT SAYS</h2>

      <figure class="testimonial" style="left:90px">
        <div class="avatar" role="img" aria-label="Portrait photo of a happy client"></div>
        <blockquote class="quote">The mix kept everyone dancing all night long and cost a fraction of a DJ.<cite>Jenna M.</cite></blockquote>
      </figure>
      <figure class="testimonial" style="left:468px">
        <div class="avatar" role="img" aria-label="Portrait photo of a happy client"></div>
        <blockquote class="quote">So easy to order, and the music fit our wedding perfectly from start to end.<cite>Carla R.</cite></blockquote>
      </figure>
    </section>
  </main>

  <footer class="site-footer">© 2015 . SPINFREEHOST. All rights reserved.</footer>
</body>
</html>
```